Motel Sign - Front

(21/03/12 - I've edited the brief and removing the words "garden view" its not fitting in the designs I'm getting and just want the word motel to be the focus. I have a template/vision of what I want - see the whiteboard sketch of what I'm looking for uploaded today. Definitely open to creatively, new designs and different ideas but the whiteboard design I've done should be a guideline. Keep it fresh/green/white. use the sample photos of green as inspiration. Thanks)
We are a motel set in the mountain country of Victoria - Australia. The front of the motel needs a fresh look. We recently removed a large amount of the garden to expose a brick courtyard fence which the front of the courtyard faces out to the main road. Within the courtyard fence there is a wooden frame and paneling.
We want to have a new sign created to slot into the wooden frame. (see photo) its the white component.
Its a very large and unusual shape and I want to keep it simple but need to fill the in the best way possible.
The space is 940mm high and 4940mm width.
The message of the sign is simple the word "MOTEL". I want people to be able to drive past and glance in and see we are a motel straight away. So the main purpose of the sign is to say "MOTEL".
I am open to colour use to match the space and have impact. I thought a background colour should be 'off white'. I'm open to the colours used to match your design as long as it matches the brief. Maybe a garden green for the emblem.
IN BRIEF:
1) the word "MOTEL"
2) Border/Background that ties in the garden.
The design should be centred, clean and simple, doesn't have to fill the whole space as long as its balanced and centred.
I like cursive and garden like designs for this one - as long its the word MOTEL still has impact. (OPEN TO NEW IDEAS)
I am also open to different ideas and suggestions if you feel you have a better way to take advantage of this space.
The sign will be 7-8 metres from the road itself.
NOTE: the photos show the space and the painted white in the space where the sign will go. The garden in front of this space will be completely cleared.
Motel

```html
<!DOCTYPE html>
<html lang="en">
<head>
<meta charset="utf-8">
<title>Motel Sign</title>
<link href="https://fonts.googleapis.com/css2?family=Kalam:wght@700&display=swap" rel="stylesheet">
<style>
  :root {
    --sign-white: #ffffff;
    --title-red: #e3141c;
    --title-shade: #8a0a0e;
    --grass-light: #b9e07a;
    --grass-mid: #6fbf3a;
    --grass-deep: #3f8f22;
  }
  html, body {
    margin: 0;
    padding: 0;
    width: 1200px;
    height: 228px;
    overflow: hidden;
    background: var(--sign-white);
  }
  .sign {
    position: relative;
    width: 1200px;
    height: 228px;
    background: var(--sign-white);
    overflow: hidden;
  }
  .sign__garden {
    position: absolute;
    left: 0;
    right: 0;
    bottom: 0;
    height: 84px;
    background: linear-gradient(to bottom, var(--grass-light) 0%, var(--grass-mid) 45%, var(--grass-deep) 100%);
  }
  .sign__title {
    position: absolute;
    left: 0;
    right: 0;
    top: 4px;
    margin: 0;
    text-align: center;
    font-family: "Kalam", cursive;
    font-weight: 700;
    font-size: 168px;
    line-height: 1;
    letter-spacing: 2px;
    color: var(--title-red);
    text-shadow: 3px 3px 0 var(--title-shade);
    transform: skewX(-8deg);
    z-index: 1;
  }
</style>
</head>
<body>
  <div class="sign">
    <h1 class="sign__title">Motel</h1>
    <div class="sign__garden" role="img" aria-label="Strip of green grass with small white and yellow daisies along the bottom edge"></div>
  </div>
</body>
</html>
```